Top of the line business card design needed for real estate brokerage

We currently have a business card with our logo but would like to have a revised version. We would love for you to implement your own design that will catch anyone's attention. The theme colors should be black, royal blue, gray/silver, and white.The contact information should be the same as the info on our current business card (picture attached). In the design that we pick, we will need to be able to edit the text so that we can customize the text content for each of our agents. Same goes for the professional picture. There should be an area on the card that each agent can have their professional portrait attached. Please include a version without the picture option as well for agents that do not wish to have a professional picture attached.

```html
<!DOCTYPE html>
<html lang="en">
<head>
<meta charset="utf-8">
<title>Clear Harbor Realty – Business Card</title>
<link rel="stylesheet" href="https://fonts.googleapis.com/css2?family=Open+Sans:wght@400;700&family=Roboto+Condensed:wght@400&display=swap">
<style>
  :root {
    --royal: #0a55b0;
    --royal-soft: #3a5bb8;
    --ink: #1f1e1f;
    --card-dark: #231f20;
    --silver: #9a9a9a;
    --skyline-light: #f1f1f1;
    --skyline-mid: #d9d9d9;
    --paper: #ffffff;
    --backdrop: #5b5b5b;
  }
  * { box-sizing: border-box; margin: 0; padding: 0; }
  html, body { width: 1200px; height: 1200px; overflow: hidden; }
  body {
    background: var(--backdrop);
    position: relative;
    font-family: "Roboto Condensed", "Arial Narrow", sans-serif;
  }
  .card {
    position: absolute;
    left: 235px;
    width: 741px;
    height: 420px;
    overflow: hidden;
  }
  .card--front { top: 151px; background: var(--paper); }
  .card--back { top: 629px; background: var(--card-dark); }

  .skyline {
    position: absolute;
    left: 0; top: 0;
    width: 513px; height: 250px;
    background: linear-gradient(180deg, var(--paper) 0%, var(--skyline-light) 45%, var(--skyline-mid) 80%, var(--paper) 100%);
  }
  .brand {
    position: absolute;
    font-family: "Open Sans", Arial, sans-serif;
    font-weight: 700;
    display: flex;
    align-items: center;
    gap: 10px;
    white-space: nowrap;
  }
  .brand__mark { width: 22px; height: 22px; background: var(--royal); flex: none; }
  .card--front .brand { left: 110px; top: 170px; font-size: 30px; color: var(--ink); }
  .card--back .brand { left: 0; right: 0; top: 150px; justify-content: center; font-size: 38px; color: #ffffff; }
  .card--back .brand__mark { width: 28px; height: 28px; background: var(--royal-soft); }

  .badge {
    position: absolute;
    left: 633px; top: 23px;
    width: 82px; height: 43px;
    border: 2px solid var(--ink);
    background: var(--paper);
  }
  .badge::before {
    content: "";
    position: absolute;
    left: 5px; top: 5px;
    width: 24px; height: 29px;
    background: var(--ink);
  }

  .agent {
    position: absolute;
    right: 46px;
    top: 232px;
    text-align: right;
  }
  .agent__name {
    font-family: "Open Sans", Arial, sans-serif;
    font-weight: 700;
    font-size: 27px;
    color: var(--royal);
    line-height: 1.1;
  }
  .agent__title { font-size: 19px; color: var(--ink); margin-top: 3px; }
  .agent-bar {
    position: absolute;
    left: 726px; top: 234px;
    width: 15px; height: 54px;
    background: var(--royal);
  }

  .contact {
    position: absolute;
    left: 26px; top: 301px;
    color: var(--ink);
    font-size: 19px;
    line-height: 1;
  }
  .contact__row { display: flex; align-items: center; gap: 18px; margin-bottom: 11px; }
  .contact__item { display: flex; align-items: center; gap: 5px; }
  .contact__item svg { width: 16px; height: 16px; fill: var(--royal); flex: none; }
  .contact__address { margin-top: 12px; }

  .base-band {
    position: absolute;
    left: 0; bottom: 0;
    width: 100%; height: 15px;
    background: var(--royal);
  }

  .services {
    position: absolute;
    left: 0; right: 0; top: 304px;
    text-align: center;
    color: #ffffff;
    font-size: 20px;
  }
  .services .sep { color: var(--royal-soft); margin: 0 4px; }
  .website {
    position: absolute;
    left: 0; right: 0; top: 342px;
    text-align: center;
    color: var(--royal-soft);
    font-size: 20px;
  }
</style>
</head>
<body>

  <section class="card card--front">
    <div class="skyline" role="img" aria-label="Line drawing of a city skyline behind the company mark"></div>
    <div class="brand"><span class="brand__mark"></span>Clear Harbor Realty</div>
    <div class="badge" aria-label="Membership badge"></div>

    <div class="agent">
      <p class="agent__name">Marlon Deveraux</p>
      <p class="agent__title">Broker</p>
    </div>
    <div class="agent-bar"></div>

    <div class="contact">
      <div class="contact__row">
        <span class="contact__item">
          <svg viewBox="0 0 16 16" aria-hidden="true"><path d="M4 0h8a1.5 1.5 0 0 1 1.5 1.5v13A1.5 1.5 0 0 1 12 16H4a1.5 1.5 0 0 1-1.5-1.5v-13A1.5 1.5 0 0 1 4 0zm0.5 2v10.5h7V2zM8 13.3a0.9 0.9 0 1 0 0 1.8 0.9 0.9 0 0 0 0-1.8z"/></svg>
          555-210-4817
        </span>
        <span class="contact__item">
          <svg viewBox="0 0 16 16" aria-hidden="true"><path d="M1 5.5C1 3 4 2 8 2s7 1 7 3.5v1.2h-3.6V5.2H4.6v1.5H1zM4.5 8h7l2 6.5h-11zM8 9.5a2 2 0 1 0 0 4 2 2 0 0 0 0-4z"/></svg>
          555-210-3362
        </span>
        <span class="contact__item">
          <svg viewBox="0 0 16 16" aria-hidden="true"><path d="M4 1h8v4H4zM1.5 6h13A1.5 1.5 0 0 1 16 7.5V12h-3v3H3v-3H0V7.5A1.5 1.5 0 0 1 1.5 6zM4.5 10.5v3h7v-3z"/></svg>
          555-210-9054
        </span>
      </div>
      <div class="contact__row">
        <span class="contact__item">
          <svg viewBox="0 0 16 16" aria-hidden="true"><path d="M0 3h16v10H0zm1.6 1.3L8 9l6.4-4.7v-0.1H1.6zM1.2 12h13.6L10 7.6 8 9 6 7.6z"/></svg>
          marlon@clearharborrealty.com
        </span>
      </div>
      <p class="contact__address">2400 Meridian Way, Suite 310 | Lakeview Shores, FL 30000</p>
    </div>

    <div class="base-band"></div>
  </section>

  <section class="card card--back">
    <div class="brand"><span class="brand__mark"></span>Clear Harbor Realty</div>
    <p class="services">Residential Real Estate<span class="sep">|</span>Commercial Real Estate<span class="sep">|</span>Property Management<span class="sep">|</span>Investment</p>
    <p class="website">WWW.CLEARHARBORREALTY.COM</p>
  </section>

</body>
</html>
```